web site to find a reliable, local tradesman, handyman or builder for any job

Design a web site as marketplace for handyman and client.
Handyman can
* set their profile (name, address, contacts)
* search / view / apply for job offers (by setting a new offer)
Client can
* search / view job offers
* generate new job offers (title, description, max price, date, duration, location).
* select and rate a job
Main functions would be SEARCH / VIEW to see in one glance WHAT needs to be done WHERE. The contractors then exchange contacts.
Handyman

```html
<!DOCTYPE html>
<html lang="en">
<head>
<meta charset="utf-8">
<title>HireLocal.de – Marketplace for handyman and client</title>
<link rel="stylesheet" href="https://fonts.googleapis.com/css2?family=Roboto:wght@300;400;500;700&display=swap">
<style>
:root{
  --orange:#f28c00;
  --orange-light:#f7a51c;
  --orange-dark:#e97800;
  --ink:#222;
  --dark:#333;
  --band:#8a8a8a;
  --paper:#ececec;
  --muted:#999;
  --white:#fff;
}
*{box-sizing:border-box;margin:0;padding:0}
html,body{width:873px;height:1200px;overflow:hidden;background:var(--paper)}
body{font-family:"Roboto",Arial,sans-serif;color:var(--ink)}
a{color:var(--orange);text-decoration:underline}
.page{position:relative;width:1000px;height:1375px;transform:scale(.873);transform-origin:0 0;background:var(--paper)}
.abs{position:absolute}

/* bands */
.top-band{left:0;top:0;width:1000px;height:227px;background:var(--band);border-top:6px solid var(--dark)}
.mid-band{left:0;top:922px;width:1000px;height:330px;background:var(--band)}
.footer{left:0;top:1252px;width:1000px;height:123px;background:var(--dark);text-align:center;color:#ddd}

/* header */
.account-btn{top:15px;width:75px;height:16px;font-size:9px;color:var(--white);text-align:center;line-height:16px;border:1px solid rgba(255,255,255,.4)}
.account-btn.signup{left:731px;background:var(--orange)}
.account-btn.signin{left:813px;background:#a0a0a0}
.brand{left:118px;top:28px;display:flex;align-items:center;gap:8px}
.brand-dot{width:30px;height:30px;border-radius:50%;background:var(--orange)}
.brand-name{font-size:24px;font-weight:700;color:var(--white)}
.nav{left:376px;top:54px;height:46px;display:flex;align-items:center}
.nav-item{font-size:12px;font-weight:500;color:var(--white);text-transform:uppercase;padding:0 23px;height:22px;line-height:22px;border-left:1px solid #bbb}
.nav-item.first{border-left:none}
.nav-item.active{background:var(--orange);height:46px;line-height:46px;width:79px;padding:0;text-align:center;color:var(--ink);font-weight:700;margin-right:2px}

/* hero */
.hero-flap{top:115px;width:12px;height:112px;background:#555}
.hero{left:105px;top:100px;width:792px;height:248px;background:var(--dark);color:var(--white)}
.hero-title{position:absolute;left:29px;top:40px;font-size:41px;font-weight:300;letter-spacing:-.5px;white-space:nowrap}
.hero-title b{font-weight:700}
.hero-sub{position:absolute;left:29px;top:82px;font-size:29px;font-weight:300;color:#ccc;white-space:nowrap}
.hero-list{position:absolute;left:29px;top:130px;list-style:none;font-size:16px;font-weight:300;color:var(--muted);line-height:19px}
.hero-list li::before{content:"-";display:inline-block;width:21px}
.hero-cta{position:absolute;left:525px;top:138px;width:232px;height:70px;background:#9a9a9a;border:2px solid #b5b5b5;text-align:center;color:var(--white);padding-top:16px}
.hero-cta strong{display:block;font-size:23px;line-height:22px}
.hero-cta span{display:block;font-size:14px;font-weight:700;line-height:14px}

/* action cards */
.card{top:357px;width:255px;height:124px;background:var(--white);padding:5px}
.card-inner{height:114px;background:linear-gradient(var(--orange-light),var(--orange-dark));padding:9px 0 0 13px;color:var(--white);overflow:hidden}
.card-title{font-size:23px;font-weight:700;line-height:26px;letter-spacing:-.6px;white-space:nowrap}
.card-sub{font-size:10.5px;font-weight:500;color:#fde3b0;white-space:nowrap;letter-spacing:-.1px}
.card-form{display:flex;margin-top:22px;height:21px}
.card-input{width:146px;background:#f2f2f2;border:1px solid #d88b1a;font-size:9px;color:#777;line-height:19px;padding-left:6px}
.card-btn{width:77px;background:var(--ink);color:var(--white);font-size:10px;font-weight:700;text-align:center;line-height:21px}
.card-link{display:block;font-size:10px;color:var(--white);margin-top:4px}

/* columns */
.col-title{font-size:23px;font-weight:700;color:var(--orange);letter-spacing:-.2px}
.skills{list-style:none;font-size:11.5px;font-weight:500}
.skills li{height:28px}
.skills li::before{content:"-";display:inline-block;width:20px}
.more-link{font-size:12px;color:var(--orange)}
.more-link::before{content:">> ";display:inline-block;margin-right:4px}
.stat{font-size:11px;line-height:24px}
.stat b{font-size:19px;margin-right:3px}
.job{font-size:10.5px;line-height:14px;color:#555;white-space:nowrap}
.job-title{font-size:12.5px;font-weight:500;color:var(--ink);line-height:16px}
.job-body{padding-left:17px}
.job b{color:var(--ink);font-weight:700}
.tour-item{width:240px}
.tour-head{font-size:11.5px;font-weight:500}
.tour-row{display:flex;gap:10px;margin-top:12px;font-size:10.5px;color:#555;line-height:14px}
.tour-row svg{flex:none}

/* testimonials */
.mid-title{left:125px;top:958px;font-size:28px;font-weight:300;color:var(--ink);letter-spacing:-.5px}
.mid-title b{font-weight:700}
.mid-text{left:125px;top:1001px;width:750px;font-size:11px;line-height:14px;color:#222}
.quote{top:1055px;width:180px;height:153px}
.quote-box{position:absolute;left:0;top:0;width:180px;height:125px;background:linear-gradient(#5a5a5a,#2e2e2e);border:1px solid #6c6c6c;color:#e4e4e4;font-size:11px;font-weight:300;line-height:14px;padding:10px 6px 0;text-indent:15px}
.quote svg{position:absolute;left:0;top:124px}

/* footer */
.foot-nav{margin-top:28px;font-size:11.5px;color:#eee}
.foot-nav span{margin:0 12px}
.foot-legal{margin-top:12px;font-size:9px;color:#999}
.foot-copy{margin-top:12px;font-size:9px;color:#999}
</style>
</head>
<body>
<div class="page">
  <div class="abs top-band"></div>

  <header>
    <div class="abs account-btn signup">SIGN UP</div>
    <div class="abs account-btn signin">SIGN IN</div>
    <div class="abs brand"><div class="brand-dot"></div><div class="brand-name">hirelocal.de</div></div>
    <nav class="abs nav">
      <div class="nav-item active">Home</div>
      <div class="nav-item first">Find a Handyman</div>
      <div class="nav-item">Find Work</div>
      <div class="nav-item">About Us</div>
      <div class="nav-item">Help</div>
    </nav>
  </header>

  <div class="abs hero-flap" style="left:94px"></div>
  <div class="abs hero-flap" style="left:894px"></div>
  <section class="abs hero">
    <h1 class="hero-title">A marketplace for <b>handyman</b> and <b>client</b>.</h1>
    <p class="hero-sub">The people you need are just a click away.</p>
    <ul class="hero-list">
      <li>Professional Solutions</li>
      <li>Hassle-Free Management</li>
      <li>Top-Notch Services</li>
      <li>Piece of Mind</li>
    </ul>
    <div class="hero-cta"><strong>LEARN MORE</strong><span>ABOUT US</span></div>
  </section>

  <section class="abs card" style="left:110px">
    <div class="card-inner">
      <div class="card-title">FIND A HANDYMAN</div>
      <div class="card-sub">SEARCH FOR THE WORKERS YOU NEED</div>
      <div class="card-form"><div class="card-input">keywords ...</div><div class="card-btn">SEARCH</div></div>
      <a class="card-link">Adcanced Search</a>
    </div>
  </section>
  <section class="abs card" style="left:375px">
    <div class="card-inner">
      <div class="card-title">FIND A JOB</div>
      <div class="card-sub">SEARCH AND APPLY FOR JOBS</div>
      <div class="card-form"><div class="card-input">keywords ...</div><div class="card-btn">SEARCH</div></div>
      <a class="card-link">Adcanced Search</a>
    </div>
  </section>
  <section class="abs card" style="left:638px">
    <div class="card-inner">
      <div class="card-title">SIGN UP</div>
      <div class="card-sub">CREATE YOUR OWN PROFILE</div>
      <div class="card-form"><div class="card-input">email address</div><div class="card-btn">SIGN UP</div></div>
    </div>
  </section>

  <h2 class="abs col-title" style="left:125px;top:518px">POPULAR SKILLS</h2>
  <ul class="abs skills" style="left:135px;top:556px">
    <li>General Contractor / Inspections</li>
    <li>Drywall and Painting</li>
    <li>Flooring</li>
    <li>Concrete and Pavement</li>
  </ul>
  <a class="abs more-link" style="left:128px;top:669px">Browse Handymen</a>

  <h2 class="abs col-title" style="left:125px;top:719px">TODAY'S STATS</h2>
  <div class="abs" style="left:125px;top:760px">
    <div class="stat"><b>68,961</b> Jobs Posted (last 30 days)</div>
    <div class="stat"><b>1,489,248</b> Registered Contractors</div>
    <div class="stat"><b>$546,908</b> Work Done (to-date)</div>
  </div>
  <a class="abs more-link" style="left:125px;top:846px">Learn More</a>

  <h2 class="abs col-title" style="left:390px;top:518px">RECENT JOBS</h2>
  <div class="abs job" style="left:401px;top:557px">
    <div class="job-title">[ Roofer Needed for 1950s Home ]</div>
    <div class="job-body"><b>Location:</b> Raleigh NC<br><b>Description:</b> Lorem ipsum dolor sit amet,<br>sectetur adipiscing elit. Proin eleifend<br>tum nibh eu condimentum... <a>read more</a></div>
  </div>
  <div class="abs job" style="left:401px;top:642px">
    <div class="job-title">[ Deck needed for my home]</div>
    <div class="job-body"><b>Location:</b> Washington DC<br><b>Description:</b> Lorem ipsum dolor sit amet,<br>sectetur adipiscing elit. Proin eleifend<br>tum nibh eu condimentum... <a>read more</a></div>
  </div>
  <div class="abs job" style="left:401px;top:727px">
    <div class="job-title">[ I need a contractor for my basement ]</div>
    <div class="job-body"><b>Location:</b> New York, NY<br><b>Description:</b> Lorem ipsum dolor sit amet,<br>sectetur adipiscing elit. Proin eleifend<br>tum nibh eu condimentum... <a>read more</a></div>
  </div>
  <a class="abs more-link" style="left:393px;top:814px">Browse Job Listings</a>

  <h2 class="abs col-title" style="left:655px;top:518px">TAKE A TOUR</h2>
  <div class="abs tour-item" style="left:665px;top:557px">
    <div class="tour-head">Post your job for free.</div>
    <div class="tour-row">
      <svg width="34" height="30" viewBox="0 0 34 30" aria-hidden="true"><circle cx="12" cy="9" r="6" fill="#8a8a8a"/><path d="M1 28c0-8 5-11 11-11s11 3 11 11z" fill="#8a8a8a"/><circle cx="23" cy="8" r="5" fill="#b5b5b5"/><path d="M20 16c7 0 13 2 13 11h-8c0-5-2-8-5-11z" fill="#b5b5b5"/></svg>
      <div>Post unlimited jobs.<br>Get the skills you need, on-demand.</div>
    </div>
  </div>
  <div class="abs tour-item" style="left:665px;top:640px">
    <div class="tour-head">Get things done faster.</div>
    <div class="tour-row">
      <svg width="34" height="32" viewBox="0 0 34 32" aria-hidden="true"><circle cx="17" cy="18" r="12" fill="none" stroke="#8a8a8a" stroke-width="3"/><path d="M17 11v8h6" fill="none" stroke="#8a8a8a" stroke-width="2.5"/><circle cx="6" cy="5" r="4" fill="#8a8a8a"/><circle cx="28" cy="5" r="4" fill="#8a8a8a"/></svg>
      <div>Get proposals right away.<br>&nbsp;Hire great talent and get the job done.</div>
    </div>
  </div>
  <div class="abs tour-item" style="left:665px;top:723px">
    <div class="tour-head">Pay only for results. Guaranteed.</div>
    <div class="tour-row">
      <svg width="34" height="36" viewBox="0 0 34 36" aria-hidden="true"><rect x="4" y="5" width="24" height="29" rx="2" fill="#fff" stroke="#8a8a8a" stroke-width="2.5"/><rect x="11" y="2" width="10" height="6" rx="1" fill="#8a8a8a"/><text x="16" y="27" font-family="Roboto,Arial,sans-serif" font-size="15" font-weight="700" fill="#8a8a8a" text-anchor="middle">$</text></svg>
      <div>View progress in real time.<br>&nbsp;Pay only after you approve the work.</div>
    </div>
  </div>
  <a class="abs more-link" style="left:658px;top:822px">About Us</a>

  <div class="abs mid-band"></div>
  <h2 class="abs mid-title">Companies of all sizes use <b>HireLocal.de</b> every day</h2>
  <p class="abs mid-text">Lorem ipsum dolor sit amet, consectetur adipiscing elit. Proin eleifend fermentum nibh eu condimentum. Aliquam id tempus justo. Pellentesque eros felis, aliquam id ullamcorper vel, varius quis quam. Pellentesque habitant morbi tristique senectus et netus et malesuada fames ac turpis egestas.</p>

  <div class="abs quote" style="left:122px">
    <div class="quote-box">“Praesent et mauris sed lorem dignissim mattis. Vivamus id luctus orci. Cras ac urna euismod arcu vehicula porttitor eget et metus. Aenean risus libero, vehicula eget placerat sed, elementum ut augue.”</div>
    <svg width="34" height="30" viewBox="0 0 34 30" aria-hidden="true"><path d="M0 0h34L0 29z" fill="#2e2e2e"/></svg>
  </div>
  <div class="abs quote" style="left:310px">
    <div class="quote-box">“Praesent et mauris sed lorem dignissim mattis. Vivamus id luctus orci. Cras ac urna euismod arcu vehicula porttitor eget et metus. Aenean risus libero, vehicula eget placerat sed, elementum ut augue.”</div>
    <svg width="34" height="30" viewBox="0 0 34 30" aria-hidden="true"><path d="M0 0h34L0 29z" fill="#2e2e2e"/></svg>
  </div>
  <div class="abs quote" style="left:496px">
    <div class="quote-box">“Praesent et mauris sed lorem dignissim mattis. Vivamus id luctus orci. Cras ac urna euismod arcu vehicula porttitor eget et metus. Aenean risus libero, vehicula eget placerat sed, elementum ut augue.”</div>
    <svg width="34" height="30" viewBox="0 0 34 30" aria-hidden="true"><path d="M0 0h34L0 29z" fill="#2e2e2e"/></svg>
  </div>
  <div class="abs quote" style="left:684px">
    <div class="quote-box">“Praesent et mauris sed lorem dignissim mattis. Vivamus id luctus orci. Cras ac urna euismod arcu vehicula porttitor eget et metus. Aenean risus libero, vehicula eget placerat sed, elementum ut augue.”</div>
    <svg width="34" height="30" viewBox="0 0 34 30" aria-hidden="true"><path d="M0 0h34L0 29z" fill="#2e2e2e"/></svg>
  </div>

  <footer class="abs footer">
    <div class="foot-nav">Home<span>|</span>Find a Handyman<span>|</span>Find Work<span>|</span>About Us<span>|</span>Help</div>
    <div class="foot-legal">Terms of Service | Trust &amp; Safety | Privacy | Site Map | FaQ</div>
    <div class="foot-copy">© 1999 - 2012 HireLocal.de. All Rights Reserved.</div>
  </footer>
</div>
</body>
</html>
```